Vorlume is about building a community in the events space.

Looking to build Sildavora.com style website, with the following key features / functionality:
• Sign up / sign in page
• Profile pages - User / Speaker / Event Organiser
• Event categories and listings
• Ratings / Review Comments

Preferably for Wordpress platform, as in Wordpress plugin, with PHP access.

Target Market(s)

Event communities

Industry/Entity Type

Building

Coding

Coded - Design and coding required

Number of Pages Required

5+ page

Font styles to use
Sans Serif

Colors
0492cd

Requirements
Must have
• Vorlume is about building a community in the events space.
• Looking to build Sildavora.com style website, with the following key features / functionality:
• • Sign up / sign in page
• • Profile pages - User / Speaker / Event Organiser
• • Event categories and listings
• • Ratings / Review Comments
• Preferably for Wordpress platform, as in Wordpress plugin, with PHP access.

```html
<!DOCTYPE html>
<html lang="en">
<head>
<meta charset="utf-8">
<title>Vorlume – Events</title>
<link href="https://fonts.googleapis.com/css2?family=Montserrat:wght@300;400;500;600;700&display=swap" rel="stylesheet">
<style>
:root{
  --brand:#0492cd;
  --brand-light:#2ea8f2;
  --brand-grad-top:#1e9df0;
  --ink:#333;
  --muted:#666;
  --soft:#999;
  --line:#e3e3e3;
  --panel:#fff;
  --row-hi:#f4f4f4;
  --ad-red:#c4161c;
}
*{box-sizing:border-box;margin:0;padding:0}
html,body{width:982px;height:1200px;overflow:hidden;background:#fff;font-family:'Montserrat',sans-serif;color:var(--ink)}
.page{position:relative;width:982px;height:1200px}
.abs{position:absolute}

/* header */
.site-header{position:absolute;left:0;top:0;width:982px;height:82px;background:linear-gradient(180deg,var(--brand-grad-top),var(--brand-light))}
.brand-name{position:absolute;left:100px;top:28px;color:#fff;font-size:22px;font-weight:600}
.search{position:absolute;left:214px;top:28px;width:283px;height:24px;border:2px solid rgba(255,255,255,.85);display:flex;align-items:center;color:#fff;font-size:10px}
.search svg{margin:0 9px 0 11px}
.search span{border-left:1px solid rgba(255,255,255,.8);padding-left:8px;line-height:16px}
.nav-btn{position:absolute;top:28px;height:25px;border:2px solid #fff;color:#fff;font-size:10.5px;display:flex;align-items:center;justify-content:center}
.nav-link{position:absolute;top:34px;color:#fff;font-size:10.5px}
.nav-sep{position:absolute;left:632px;top:33px;width:1px;height:15px;background:rgba(255,255,255,.8)}
.social-ring{position:absolute;top:26px;width:28px;height:28px;border:2px solid rgba(255,255,255,.8);border-radius:50%}

/* welcome */
.welcome{position:absolute;left:81px;top:107px;width:820px;height:55px;border:1px solid #d9eaf5}
.welcome .title{position:absolute;left:97px;top:18px;color:var(--brand);font-size:14px;font-weight:500;white-space:nowrap}
.welcome .tag{position:absolute;left:262px;top:21px;font-size:10.5px;color:#555;white-space:nowrap}
.welcome .mail{position:absolute;left:478px;top:15px;width:188px;height:22px;border:1px solid #ccc;font-size:9px;color:#aaa;padding:5px 16px}
.btn-blue{background:linear-gradient(180deg,#36aef5,var(--brand));color:#fff;display:flex;align-items:center;justify-content:center}
.welcome .subscribe{position:absolute;left:672px;top:15px;width:92px;height:22px;font-size:12px}

/* categories */
.box{position:absolute;border:1px solid var(--line);background:var(--panel)}
.categories{left:81px;top:188px;width:175px;height:370px}
.categories h3{position:absolute;left:15px;top:10px;font-size:13px;font-weight:400;color:#444}
.cat{position:absolute;left:12px;display:flex;align-items:center;font-size:9.5px;color:#444}
.cat i{width:24px;height:22px;background:#ececec;margin-right:14px;display:flex;align-items:center;justify-content:center}
.cat i b{width:10px;height:8px;background:#555;border-radius:1px}
.more-btn{position:absolute;left:13px;top:338px;width:148px;height:19px;font-size:9.5px}

.ad-block{position:absolute;color:#fff}
.ad-red{left:82px;top:572px;width:176px;height:175px;background:var(--ad-red)}
.ad-red .n{position:absolute;left:10px;top:4px;font-size:16px;font-weight:500}
.ad-red .s{position:absolute;left:11px;top:24px;font-size:7px}
.ad-red .art{position:absolute;left:0;top:45px;width:110px;height:130px;background:linear-gradient(160deg,#f0ead0,#6b4a2c)}
.ad-red ul{position:absolute;right:5px;top:67px;list-style:none;text-align:right;font-size:8.5px;font-style:italic;line-height:12.6px}
.ad-red .u{position:absolute;right:4px;bottom:3px;font-size:8.5px;font-weight:600}
.meeting-photo{position:absolute;left:82px;top:748px;width:176px;height:162px;background:linear-gradient(180deg,#e9eef2,#b8c0c6)}
.posts-tag{position:absolute;left:125px;top:900px;width:88px;height:20px;font-size:10px;font-weight:500}
.post{position:absolute;left:81px;width:176px;height:27px;border-bottom:1px solid var(--line);font-size:8.6px;color:#333;padding:7px 0 0 13px;white-space:nowrap}
.post::before{content:"›";position:absolute;left:2px;top:5px;font-size:10px}

/* events */
.events{left:271px;top:188px;width:440px;height:845px}
.toolbar{position:absolute;left:0;top:0;width:438px;height:36px;border-bottom:1px solid var(--line)}
.filter{position:absolute;left:12px;top:7px;width:60px;height:20px;font-size:9.5px;gap:5px}
.sort{position:absolute;left:307px;top:13px;font-size:9.5px;color:#333}
.popular{position:absolute;left:379px;top:7px;width:47px;height:21px;font-size:9.5px}
.event{position:absolute;left:0;width:438px;height:126px;border-bottom:1px solid var(--line)}
.event.hi{background:var(--row-hi)}
.thumb{position:absolute;left:13px;top:19px;width:110px;height:84px}
.ev-title{position:absolute;left:141px;top:19px;font-size:17.5px;font-weight:300;color:#555;display:flex;align-items:center;gap:10px}
.loc{position:absolute;left:346px;top:23px;width:81px;height:14px;border:1px solid #8ccbf0;font-size:7.8px;color:#555;display:flex;align-items:center;justify-content:center}
.desc{position:absolute;left:142px;top:48px;font-size:8.8px;color:#666}
.votes{position:absolute;left:142px;top:85px;width:38px;height:17px;border:1px solid #777;font-size:8.8px;color:#555;display:flex;align-items:center;justify-content:center}
.rating{position:absolute;left:300px;top:84px;font-size:9px;color:#666;display:flex;align-items:center;gap:3px}
.rating .st{color:var(--brand-light);font-size:10px;letter-spacing:2px}
.pager{position:absolute;top:807px;width:72px;height:21px;font-size:9px}
.next{left:355px;border:1px solid #ddd;color:#333;display:flex;align-items:center;justify-content:center;background:#fff}

/* right */
.ad-biz{left:725px;top:189px;width:175px;height:174px;background:linear-gradient(160deg,#2fb7c6,#9fd7dd 45%,#1fa7b6)}
.ad-biz .n{position:absolute;right:10px;top:6px;font-size:8px;font-weight:700;font-style:italic}
.ad-biz .t{position:absolute;left:20px;top:118px;font-size:10px;font-style:italic;font-weight:700;line-height:12px}
.ad-biz .c{position:absolute;right:8px;top:123px;font-size:9.5px;font-weight:700;text-align:center;color:#0f4b55}
.ad-biz .c small{display:block;font-size:6.5px;font-weight:400}
.ad-biz .l{position:absolute;right:10px;bottom:4px;font-size:7px;font-style:italic}
.speakers{left:725px;top:378px;width:177px;height:497px}
.speakers h3{height:28px;background:linear-gradient(180deg,#36aef5,var(--brand-light));color:#fff;font-size:12px;font-weight:400;padding:8px 11px;margin:-1px -1px 0}
.spk{position:absolute;left:8px;width:159px;height:54px;border-bottom:1px solid #eee}
.avatar{position:absolute;left:3px;top:10px;width:34px;height:34px;border-radius:50%;background:linear-gradient(160deg,#e2c2a8,#7d5a44)}
.rank{position:absolute;left:1px;top:33px;width:14px;height:14px;border-radius:50%;background:var(--brand-light);border:1px solid #fff;color:#fff;font-size:7.5px;display:flex;align-items:center;justify-content:center}
.spk .nm{position:absolute;left:42px;top:12px;font-size:9px;font-weight:600;color:#333}
.spk .mt{position:absolute;left:42px;top:28px;font-size:7.6px;color:#777}
.spk svg{position:absolute;right:4px;top:19px}
.read{position:absolute;left:11px;top:479px;font-size:8.6px;color:#333}

/* footer */
.footer-band{position:absolute;left:79px;top:1102px;width:822px;height:50px;background:repeating-linear-gradient(135deg,#efefef 0 2px,#f7f7f7 2px 4px)}
.footer-band .we{position:absolute;left:12px;top:16px;font-size:13.5px;color:#222;white-space:nowrap}
.f-social{position:absolute;top:10px;width:30px;height:30px;border-radius:50%;background:var(--brand-light)}
.footer-band .ask{position:absolute;left:426px;top:16px;font-size:13.5px;font-weight:600;color:#222}
.footer-band .mail{position:absolute;left:609px;top:12px;width:126px;height:25px;background:#fff;border:1px solid #ccc;font-size:8.5px;color:#666;padding:7px 10px}
.footer-band .join{position:absolute;left:735px;top:12px;width:58px;height:25px;font-size:9.5px;font-weight:700}
.foot-links{position:absolute;left:93px;top:1164px;font-size:9.5px;color:#222}
.foot-links span{margin:0 12px}
.copyright{position:absolute;left:604px;top:1171px;font-size:8.8px;color:#222}
</style>
</head>
<body>
<div class="page">

<header class="site-header">
  <div class="brand-name">Vorlume</div>
  <div class="search">
    <svg width="11" height="11" viewBox="0 0 12 12"><circle cx="5" cy="5" r="3.7" fill="none" stroke="#fff" stroke-width="1.8"/><path d="M8 8l3 3" stroke="#fff" stroke-width="1.8"/></svg>
    <span>Discover your next favorite event...</span>
  </div>
  <div class="nav-btn" style="left:586px;width:37px;letter-spacing:2px">ooo</div>
  <div class="nav-sep"></div>
  <div class="nav-link" style="left:649px">Login</div>
  <div class="nav-btn" style="left:693px;width:59px">Sign Up</div>
  <div class="social-ring" style="left:775px" aria-label="Social link"></div>
  <div class="social-ring" style="left:811px" aria-label="Social link"></div>
  <div class="social-ring" style="left:847px" aria-label="Social link"></div>
</header>

<section class="welcome">
  <svg class="abs" style="left:55px;top:19px" width="32" height="16" viewBox="0 0 32 16"><text x="0" y="10" font-size="10" fill="#0492cd">"</text><path d="M9 8l15-6-4 12-4-4-7-2zM16 10l8-8" fill="none" stroke="#0492cd" stroke-width="1.3"/><text x="27" y="10" font-size="10" fill="#0492cd">"</text></svg>
  <div class="title">Welcome to Vorlume</div>
  <div class="tag">Get the events in our mail box, daily...</div>
  <div class="mail">Enter Email id</div>
  <div class="subscribe btn-blue">Subscribe</div>
</section>

<aside class="box categories">
  <h3>Event Categories</h3>
  <div class="cat" style="top:44px"><i><b></b></i>Arts</div>
  <div class="cat" style="top:73px"><i><b></b></i>Business</div>
  <div class="cat" style="top:102px"><i><b></b></i>Education</div>
  <div class="cat" style="top:130px"><i><b style="border-radius:50%;width:9px;height:9px"></b></i>Geographical</div>
  <div class="cat" style="top:159px"><i><b></b></i>Health</div>
  <div class="cat" style="top:188px"><i><b></b></i>Law</div>
  <div class="cat" style="top:217px"><i><b></b></i>Medical</div>
  <div class="cat" style="top:245px"><i><b style="border-radius:50%"></b></i>News</div>
  <div class="cat" style="top:274px"><i><b style="border-radius:50%;width:9px;height:9px"></b></i>Recreation</div>
  <div class="cat" style="top:303px"><i><b></b></i>Technology</div>
  <div class="more-btn btn-blue">More Event Categories</div>
</aside>

<div class="ad-block ad-red">
  <div class="n">brindle studio</div>
  <div class="s">[creative marketing solutions]</div>
  <div class="art" role="img" aria-label="Illustrated owl mascot"></div>
  <ul><li>web design</li><li>SEO/SEM</li><li>online media</li><li>copywriting</li><li>brand identity</li><li>public relations</li></ul>
  <div class="u">brindlestudio.net</div>
</div>
<div class="meeting-photo" role="img" aria-label="Photo of a business team meeting around a table"></div>
<div class="posts-tag btn-blue">TOP 5 POSTS</div>
<div class="post" style="top:927px">Finibus Bonorum et Malorum</div>
<div class="post" style="top:954px">Nostrum exercitationem</div>
<div class="post" style="top:981px">Duis aute irure dolor in reprehenderit</div>
<div class="post" style="top:1008px">Nor again is there anyone</div>
<div class="post" style="top:1035px">Finibus Bonorum et Malorum</div>

<main class="box events">
  <div class="toolbar">
    <div class="filter btn-blue"><svg width="13" height="13" viewBox="0 0 13 13"><path d="M3 1v11M7 1v11M11 1v11" stroke="#fff"/><rect x="1.5" y="3" width="3" height="2" fill="#fff"/><rect x="5.5" y="8" width="3" height="2" fill="#fff"/><rect x="9.5" y="4" width="3" height="2" fill="#fff"/></svg>Filter</div>
    <div class="sort">Relevance &nbsp;/</div>
    <div class="popular btn-blue">Popular</div>
  </div>

  <article class="event hi" style="top:36px">
    <div class="thumb" role="img" aria-label="Concert crowd under stage lights" style="background:linear-gradient(180deg,#c9441c,#3a120a)"></div>
    <div class="ev-title"><svg width="10" height="13" viewBox="0 0 10 13"><path d="M1 1h8v11l-4-3-4 3z" fill="none" stroke="#2ea8f2" stroke-width="1.4"/></svg>Event Name</div>
    <div class="loc">Sydney,Australia</div>
    <div class="desc">Lorem ipsum dolor sit amet, consectetur adipiscing elit....</div>
    <div class="votes">▲534</div>
    <div class="rating"><span class="st">★★★★☆</span>(133) <span style="color:#2ea8f2">◯</span>(26)</div>
  </article>
  <article class="event" style="top:162px">
    <div class="thumb" role="img" aria-label="Speaker presenting to an audience" style="background:linear-gradient(180deg,#2a3f7a,#c0584a)"></div>
    <div class="ev-title"><svg width="10" height="13" viewBox="0 0 10 13"><path d="M1 1h8v11l-4-3-4 3z" fill="none" stroke="#2ea8f2" stroke-width="1.4"/></svg>Event Name</div>
    <div class="loc">Sydney,Australia</div>
    <div class="desc">Lorem ipsum dolor sit amet, consectetur adipiscing elit....</div>
    <div class="votes">▲534</div>
    <div class="rating"><span class="st">★★★★☆</span>(133) <span style="color:#2ea8f2">◯</span>(26)</div>
  </article>
  <article class="event" style="top:287px">
    <div class="thumb" role="img" aria-label="Business colleagues reviewing documents" style="background:linear-gradient(160deg,#e8e4dc,#8a7a66)"></div>
    <div class="ev-title"><svg width="10" height="13" viewBox="0 0 10 13"><path d="M1 1h8v11l-4-3-4 3z" fill="none" stroke="#2ea8f2" stroke-width="1.4"/></svg>Event Name</div>
    <div class="loc">Sydney,Australia</div>
    <div class="desc">Lorem ipsum dolor sit amet, consectetur adipiscing elit....</div>
    <div class="votes">▲534</div>
    <div class="rating"><span class="st">★★★★☆</span>(133) <span style="color:#2ea8f2">◯</span>(26)</div>
  </article>
  <article class="event" style="top:412px">
    <div class="thumb" role="img" aria-label="Banquet hall lit in purple" style="background:linear-gradient(180deg,#7a3fc2,#2a1448)"></div>
    <div class="ev-title"><svg width="10" height="13" viewBox="0 0 10 13"><path d="M1 1h8v11l-4-3-4 3z" fill="none" stroke="#2ea8f2" stroke-width="1.4"/></svg>Event Name</div>
    <div class="loc">Sydney,Australia</div>
    <div class="desc">Lorem ipsum dolor sit amet, consectetur adipiscing elit....</div>
    <div class="votes">▲534</div>
    <div class="rating"><span class="st">★★★★☆</span>(133) <span style="color:#2ea8f2">◯</span>(26)</div>
  </article>
  <article class="event" style="top:537px">
    <div class="thumb" role="img" aria-label="Networking reception with guests in suits" style="background:linear-gradient(180deg,#d8d8d6,#6e6e6c)"></div>
    <div class="ev-title"><svg width="10" height="13" viewBox="0 0 10 13"><path d="M1 1h8v11l-4-3-4 3z" fill="none" stroke="#2ea8f2" stroke-width="1.4"/></svg>Event Name</div>
    <div class="loc">Sydney,Australia</div>
    <div class="desc">Lorem ipsum dolor sit amet, consectetur adipiscing elit....</div>
    <div class="votes">▲534</div>
    <div class="rating"><span class="st">★★★★☆</span>(133) <span style="color:#2ea8f2">◯</span>(26)</div>
  </article>
  <article class="event" style="top:662px">
    <div class="thumb" role="img" aria-label="Festive holiday party" style="background:linear-gradient(160deg,#b5262a,#2a1a14)"></div>
    <div class="ev-title"><svg width="10" height="13" viewBox="0 0 10 13"><path d="M1 1h8v11l-4-3-4 3z" fill="none" stroke="#2ea8f2" stroke-width="1.4"/></svg>Event Name</div>
    <div class="loc">Sydney,Australia</div>
    <div class="desc">Lorem ipsum dolor sit amet, consectetur adipiscing elit....</div>
    <div class="votes">▲534</div>
    <div class="rating"><span class="st">★★★★☆</span>(133) <span style="color:#2ea8f2">◯</span>(26)</div>
  </article>

  <div class="pager btn-blue" style="left:15px">PREVIOUS</div>
  <div class="pager next">NEXT</div>
</main>

<div class="ad-block ad-biz">
  <div class="abs" role="img" aria-label="Photo of a smiling business team" style="left:0;top:18px;width:175px;height:100px;background:linear-gradient(180deg,rgba(255,255,255,.25),rgba(120,130,140,.45))"></div>
  <div class="n">KESTRALO</div>
  <div class="t">The Best Place<br>To Start<br>Your Business!</div>
  <div class="c"><small>Call Us:</small>555-010-482</div>
  <div class="l">Learn More »</div>
</div>

<aside class="box speakers">
  <h3>TRENDING SPEAKERS</h3>
  <div class="spk" style="top:28px"><div class="avatar" role="img" aria-label="Speaker portrait"></div><div class="rank">1</div><div class="nm">Telva Ordane</div><div class="mt">Reviews 2 , Followers 5</div><svg width="13" height="10" viewBox="0 0 13 10"><circle cx="5" cy="3" r="2.5" fill="#888"/><path d="M0 10c0-3 2-4 5-4s5 1 5 4z" fill="#888"/><path d="M10 3v4M8 5h4" stroke="#888" stroke-width="1.3"/></svg></div>
  <div class="spk" style="top:82px"><div class="avatar" role="img" aria-label="Speaker portrait"></div><div class="rank">2</div><div class="nm">Telva Ordane</div><div class="mt">Reviews 2 , Followers 5</div><svg width="13" height="10" viewBox="0 0 13 10"><circle cx="5" cy="3" r="2.5" fill="#888"/><path d="M0 10c0-3 2-4 5-4s5 1 5 4z" fill="#888"/><path d="M10 3v4M8 5h4" stroke="#888" stroke-width="1.3"/></svg></div>
  <div class="spk" style="top:135px"><div class="avatar" role="img" aria-label="Speaker portrait"></div><div class="rank">3</div><div class="nm">Telva Ordane</div><div class="mt">Reviews 2 , Followers 5</div><svg width="13" height="10" viewBox="0 0 13 10"><circle cx="5" cy="3" r="2.5" fill="#888"/><path d="M0 10c0-3 2-4 5-4s5 1 5 4z" fill="#888"/><path d="M10 3v4M8 5h4" stroke="#888" stroke-width="1.3"/></svg></div>
  <div class="spk" style="top:188px"><div class="avatar" role="img" aria-label="Speaker portrait"></div><div class="rank">4</div><div class="nm">Telva Ordane</div><div class="mt">Reviews 2 , Followers 5</div><svg width="13" height="10" viewBox="0 0 13 10"><circle cx="5" cy="3" r="2.5" fill="#888"/><path d="M0 10c0-3 2-4 5-4s5 1 5 4z" fill="#888"/><path d="M10 3v4M8 5h4" stroke="#888" stroke-width="1.3"/></svg></div>
  <div class="spk" style="top:244px"><div class="avatar" role="img" aria-label="Speaker portrait"></div><div class="rank">5</div><div class="nm">Telva Ordane</div><div class="mt">Reviews 2 , Followers 5</div><svg width="13" height="10" viewBox="0 0 13 10"><circle cx="5" cy="3" r="2.5" fill="#888"/><path d="M0 10c0-3 2-4 5-4s5 1 5 4z" fill="#888"/><path d="M10 3v4M8 5h4" stroke="#888" stroke-width="1.3"/></svg></div>
  <div class="spk" style="top:297px"><div class="avatar" role="img" aria-label="Speaker portrait"></div><div class="rank">6</div><div class="nm">Telva Ordane</div><div class="mt">Reviews 2 , Followers 5</div><svg width="13" height="10" viewBox="0 0 13 10"><circle cx="5" cy="3" r="2.5" fill="#888"/><path d="M0 10c0-3 2-4 5-4s5 1 5 4z" fill="#888"/><path d="M10 3v4M8 5h4" stroke="#888" stroke-width="1.3"/></svg></div>
  <div class="spk" style="top:350px"><div class="avatar" role="img" aria-label="Speaker portrait"></div><div class="rank">7</div><div class="nm">Telva Ordane</div><div class="mt">Reviews 2 , Followers 5</div><svg width="13" height="10" viewBox="0 0 13 10"><circle cx="5" cy="3" r="2.5" fill="#888"/><path d="M0 10c0-3 2-4 5-4s5 1 5 4z" fill="#888"/><path d="M10 3v4M8 5h4" stroke="#888" stroke-width="1.3"/></svg></div>
  <div class="spk" style="top:406px"><div class="avatar" role="img" aria-label="Speaker portrait"></div><div class="rank">8</div><div class="nm">Telva Ordane</div><div class="mt">Reviews 2 , Followers 5</div><svg width="13" height="10" viewBox="0 0 13 10"><circle cx="5" cy="3" r="2.5" fill="#888"/><path d="M0 10c0-3 2-4 5-4s5 1 5 4z" fill="#888"/><path d="M10 3v4M8 5h4" stroke="#888" stroke-width="1.3"/></svg></div>
  <div class="read">Read More</div>
</aside>

<footer>
  <div class="footer-band">
    <div class="we">@we are Vorlume</div>
    <div class="f-social" style="left:142px" aria-label="Social link"></div>
    <div class="f-social" style="left:178px" aria-label="Social link"></div>
    <div class="f-social" style="left:214px" aria-label="Social link"></div>
    <div class="ask">Do you Love our Events?</div>
    <div class="mail">Enter Email id</div>
    <div class="join btn-blue">Join Now</div>
  </div>
  <div class="foot-links">About Us<span>:</span>Contact Us<span>:</span>Team<span>:</span>Careers</div>
  <div class="copyright">Copyrights © 2017, www.vorlume-events.net. All Rights Reserved.</div>
</footer>

</div>
</body>
</html>
```